Construction Contractor
Bayt Nuwaris
Professional
Fahad Omar Qurashi
Owner
Rawda Street P.O.Box 483920 Jeddah 24719 Saudi Arabia
baytnuwaris@mailbox-example.com
We need Logo to be in the middle and company name under the logo

```html
<!DOCTYPE html>
<html lang="en">
<head>
<meta charset="utf-8">
<title>Bayt Nuwaris — Stationery</title>
<link rel="stylesheet" href="https://fonts.googleapis.com/css2?family=Montserrat:wght@400;600;700&display=swap">
<style>
  :root{
    --brown:#5b3b22;
    --gold:#c6a15b;
    --paper:#ffffff;
    --edge:#e4e2df;
    --ink:#6b5a4c;
    --faint:#e9e4dc;
    --bg:#ffffff;
  }
  *{box-sizing:border-box;margin:0;padding:0}
  html,body{width:1200px;height:936px;overflow:hidden;background:var(--bg)}
  body{position:relative;font-family:"Montserrat",Arial,sans-serif}
  .sheet{position:absolute;background:var(--paper);border:1px solid var(--edge);overflow:hidden}
  .sheet svg.deco{position:absolute;left:0;top:0;width:100%;height:100%}
  .brandname{font-family:"Montserrat",Arial,sans-serif;font-weight:700;color:var(--brown);letter-spacing:.04em;white-space:nowrap;text-transform:uppercase}
  .brandmark{display:flex;flex-direction:column;align-items:center;position:absolute}
  .brandmark .square{background:var(--brown)}
  .smalltext{font-size:5.5px;line-height:1.6;color:var(--ink);white-space:nowrap}

  /* letterhead */
  .letterhead{left:183px;top:68px;width:388px;height:546px}
  .letterhead .brandmark{left:22px;top:40px;align-items:flex-start}
  .letterhead .brandmark .square{width:22px;height:22px;margin-bottom:5px}
  .letterhead .brandname{font-size:11px}
  .letterhead .contact{position:absolute;right:18px;top:24px}
  .letterhead .watermark{position:absolute;left:0;right:0;top:270px;text-align:center;font-size:26px;font-weight:700;color:var(--faint);letter-spacing:.04em;text-transform:uppercase}

  /* folder */
  .folder{left:634px;top:38px;width:465px;height:576px}
  .folder .brandmark{left:120px;right:0;top:228px}
  .folder .brandmark .square{width:46px;height:46px;margin-bottom:14px}
  .folder .brandname{font-size:26px}

  /* business cards */
  .card-front{left:43px;top:665px;width:180px;height:91px}
  .card-front .person{position:absolute;left:22px;top:9px;font-size:5px;line-height:1.5}
  .card-front .person .name{font-size:6px;font-weight:600;color:var(--brown)}
  .card-front .brandmark{right:16px;top:50px}
  .card-front .brandmark .square{width:14px;height:14px;margin-bottom:4px}
  .card-front .brandname{font-size:7px}
  .card-back{left:43px;top:776px;width:180px;height:102px}
  .card-back .watermark{position:absolute;left:0;right:0;top:30px;text-align:center;font-size:13px;font-weight:700;color:var(--faint);text-transform:uppercase;letter-spacing:.04em}
  .card-back .web{position:absolute;left:0;right:0;bottom:10px;text-align:center;font-size:6px;color:var(--ink);letter-spacing:.08em}

  /* envelopes */
  .envelope-front{left:266px;top:672px;width:437px;height:206px}
  .envelope-front .brandmark{left:40px;top:50px;align-items:flex-start}
  .envelope-front .brandmark .square{width:26px;height:26px;margin-bottom:8px}
  .envelope-front .brandname{font-size:14px}
  .envelope-front .tagline{font-size:6px;color:var(--gold);letter-spacing:.12em;text-transform:uppercase;margin-top:3px}
  .envelope-front .smalltext{margin-top:2px}
  .envelope-back{left:736px;top:672px;width:436px;height:206px}
  .envelope-back .web{position:absolute;left:0;right:0;top:22px;text-align:center;font-size:11px;color:#fff;letter-spacing:.22em}
</style>
</head>
<body>

<section class="sheet letterhead" aria-label="Letterhead">
  <div class="brandmark">
    <span class="square"></span>
    <span class="brandname">Bayt Nuwaris</span>
  </div>
  <div class="contact smalltext">
    Fahad Omar Qurashi<br>Owner<br>Rawda Street P.O.Box 483920<br>Jeddah 24719 Saudi Arabia<br>baytnuwaris@mailbox-example.com<br>www.baytnuwaris.example
  </div>
  <div class="watermark">Bayt Nuwaris</div>
  <svg class="deco" viewBox="0 0 388 546" preserveAspectRatio="none" aria-hidden="true">
    <path d="M0 532 C110 500 230 470 388 486 L388 546 L0 546 Z" fill="var(--brown)"/>
    <path d="M0 524 C110 492 230 462 388 478" fill="none" stroke="var(--gold)" stroke-width="1.5"/>
  </svg>
</section>

<section class="sheet folder" aria-label="Presentation folder">
  <svg class="deco" viewBox="0 0 465 576" preserveAspectRatio="none" aria-hidden="true">
    <path d="M0 0 L22 0 C60 80 50 180 26 280 C8 360 10 450 40 576 L0 576 Z" fill="var(--brown)"/>
    <path d="M22 0 C68 80 58 180 34 280 C16 360 18 450 48 576" fill="none" stroke="var(--gold)" stroke-width="1.5"/>
  </svg>
  <div class="brandmark">
    <span class="square"></span>
    <span class="brandname">Bayt Nuwaris</span>
  </div>
</section>

<section class="sheet card-front" aria-label="Business card front">
  <svg class="deco" viewBox="0 0 180 91" preserveAspectRatio="none" aria-hidden="true">
    <path d="M0 0 L12 0 C20 30 14 60 4 91 L0 91 Z" fill="var(--brown)"/>
    <path d="M12 0 C22 30 16 60 7 91" fill="none" stroke="var(--gold)" stroke-width="0.8"/>
  </svg>
  <div class="person smalltext">
    <div class="name">Fahad Omar Qurashi</div>
    Owner<br>Rawda Street, Jeddah<br>baytnuwaris@mailbox-example.com
  </div>
  <div class="brandmark">
    <span class="square"></span>
    <span class="brandname">Bayt Nuwaris</span>
  </div>
</section>

<section class="sheet card-back" aria-label="Business card back">
  <div class="watermark">Bayt Nuwaris</div>
  <div class="web">www.baytnuwaris.example</div>
</section>

<section class="sheet envelope-front" aria-label="Envelope front">
  <svg class="deco" viewBox="0 0 437 206" preserveAspectRatio="none" aria-hidden="true">
    <path d="M437 0 L400 0 C425 60 420 140 395 206 L437 206 Z" fill="var(--brown)"/>
    <path d="M394 0 C419 60 414 140 389 206" fill="none" stroke="var(--gold)" stroke-width="1.2"/>
  </svg>
  <div class="brandmark">
    <span class="square"></span>
    <span class="brandname">Bayt Nuwaris</span>
    <span class="tagline">Construction Contractor</span>
    <span class="smalltext">Rawda Street P.O.Box 483920 Jeddah</span>
  </div>
</section>

<section class="sheet envelope-back" aria-label="Envelope back">
  <svg class="deco" viewBox="0 0 436 206" preserveAspectRatio="none" aria-hidden="true">
    <path d="M0 0 L436 0 L436 62 C300 72 140 74 0 62 Z" fill="var(--brown)"/>
    <path d="M0 68 C140 80 300 78 436 68" fill="none" stroke="var(--gold)" stroke-width="1.2"/>
  </svg>
  <div class="web">www.baytnuwaris.example</div>
</section>

</body>
</html>
```